Macadamia Nuts Doypack Design

Trovella grows, processes and trades macadamia nuts globally (www.trovella-example.com). We mainly supply the nuts to packaging factories, who does final packaging for retailers. However we want to re-enter the retail market (which we have previously been active in) by offering macadamia nuts in shell within plastic pouch (“doypack”) – BUT we will also include a nice handcracker for free. Macadamia nuts are difficult to crack, and therefore a very special and rare aluminium cracker has been designed. This is a unique offering –nice twist on well known product.
To this end we are looking for a new or refreshed design of our previous retail range. This will be offered to the market during a trade show in Paris in 18-23 October 2014
WE ADDED AN OLD DESIGN - DONT JUST AMEND THE ELEMENTS AND GIVE IT BACK. THIS IS ONLY TO SHOW YOU SOME OF THE LEGAL REQUIREMENTS on retail packaging. We want a much better design than this.
Updates

Dear designers: 3 things to note: - please have a cutout (window) on the front of the pack where the macadamia nuts (product in bag) is visible. This window is essential because the product we offer is unique in that it is unusual to sell it in shell. Consumers need to see it. - We need the window large enough to make the free hand cracker visible (around 20-25% of the front view). - It emerged that the macadamia in shell picture with leaves used non-macadamia leaves. Therefore please don't use that image. I will upload other images of the product in shell. Thanks Anton

Hi all, thank you for the designs, our office will now create a final shortlist and revert back to you. Anton

Target Market(s)

Middle income health conscious buyers looking for a special snack product. It can also be used as a gift (e.g. airport duty free shops).

Industry/Entity Type

Legal

Font styles to use
Sans Serif

Colors
cadf82
faf289
faee3f
add136
f6faec
e9f1ce
fdf9cf
fee18a
9bcb3c

Requirements
Must have
• Comply with legal packaging requirements as per the attached briefing document (see sec ion on mandatory elements
Reference to the free nut cracker (see attached picture of steel photo)
Should not have
• Old style "farmhouse" design

```html
<!DOCTYPE html>
<html lang="en">
<head>
<meta charset="UTF-8">
<title>Trovella Macadamia Nuts – Doypack Front</title>
<link rel="stylesheet" href="https://fonts.googleapis.com/css2?family=Ranchers&family=Pathway+Gothic+One&family=Oswald:wght@500&display=swap">
<style>
  :root {
    --backdrop: #e4e4e4;
    --gold: #d9aa22;
    --red: #a82a2a;
    --red-dark: #7d1b1b;
    --brown: #6b4316;
    --cream: #fbf6ea;
    --ink: #3a3a3a;
    --white: #ffffff;
    --tag: #e6a91c;
  }
  * { box-sizing: border-box; margin: 0; padding: 0; }
  html, body {
    width: 1200px; height: 1200px; overflow: hidden;
    background: var(--backdrop);
  }
  .canvas {
    position: relative; width: 1200px; height: 1200px;
    background: radial-gradient(circle at 50% 40%, #f1f1f1, var(--backdrop));
  }
  .pouch {
    position: absolute; left: 290px; top: 80px;
    width: 630px; height: 1040px;
  }
  .pouch-shape { position: absolute; inset: 0; }
  .brand-box {
    position: absolute; left: 202px; top: 82px;
    width: 226px; height: 84px;
    background: var(--white); border-radius: 10px;
    display: flex; align-items: center; justify-content: center; gap: 12px;
  }
  .brand-dot { width: 30px; height: 30px; border-radius: 50%; background: var(--gold); }
  .brand-name {
    font-family: "Oswald", sans-serif; font-weight: 500;
    font-size: 30px; color: var(--brown); letter-spacing: 0.5px;
  }
  .product-title {
    position: absolute; left: 0; right: 0; top: 176px;
    text-align: center; font-family: "Ranchers", sans-serif; font-weight: 400;
    color: var(--cream); line-height: 0.92;
    text-shadow:
      3px 3px 0 var(--brown), -3px -3px 0 var(--brown),
      3px -3px 0 var(--brown), -3px 3px 0 var(--brown),
      0 4px 0 var(--brown), 0 -4px 0 var(--brown),
      4px 0 0 var(--brown), -4px 0 0 var(--brown),
      5px 8px 6px rgba(0,0,0,0.35);
  }
  .title-line-1 { display: block; font-size: 96px; letter-spacing: 1px; }
  .title-line-2 { display: block; font-size: 128px; letter-spacing: 2px; }
  .benefits {
    position: absolute; left: 0; right: 0; top: 462px;
    list-style: none; text-align: center;
    font-family: "Pathway Gothic One", sans-serif;
    font-size: 19px; color: var(--ink);
  }
  .benefits li { height: 34px; line-height: 34px; }
  .product-photo {
    position: absolute; left: 60px; top: 640px;
    width: 500px; height: 268px; border-radius: 50%;
    background: radial-gradient(ellipse at 50% 42%, #8a6238 0%, #7a6a34 35%, #5e8a34 60%, #3f7d2a 72%, rgba(63,125,42,0) 74%);
  }
  .net-weight {
    position: absolute; left: 30px; top: 974px;
    font-family: "Oswald", sans-serif; font-weight: 500;
    font-size: 27px; color: var(--cream);
  }
  .free-tag {
    position: absolute; left: 278px; top: 972px;
    width: 196px; height: 48px; background: var(--tag);
    clip-path: polygon(8% 0, 100% 0, 100% 100%, 0 100%);
    font-family: "Ranchers", sans-serif; font-size: 26px;
    color: var(--white); display: flex; align-items: center; justify-content: center;
    padding-left: 12px;
  }
  .cracker-preview {
    position: absolute; left: 482px; top: 912px;
    width: 108px; height: 96px; border-radius: 12px;
    background: linear-gradient(135deg, #fafafa, #bdbdbd);
  }
</style>
</head>
<body>
<main class="canvas">
  <section class="pouch">
    <svg class="pouch-shape" viewBox="0 0 630 1040" width="630" height="1040" aria-hidden="true">
      <defs>
        <linearGradient id="goldFill" x1="0" y1="0" x2="1" y2="1">
          <stop offset="0" stop-color="#e2b52c"/>
          <stop offset="1" stop-color="#cf9f1a"/>
        </linearGradient>
        <linearGradient id="silverFill" x1="0" y1="0" x2="1" y2="0">
          <stop offset="0" stop-color="#dcdcdc"/>
          <stop offset="0.35" stop-color="#fafafa"/>
          <stop offset="0.8" stop-color="#f0f0f0"/>
          <stop offset="1" stop-color="#d6d6d6"/>
        </linearGradient>
      </defs>
      <rect x="0" y="0" width="630" height="1040" fill="url(#silverFill)"/>
      <path d="M0 0 H630 V440 Q370 385 0 450 Z" fill="url(#goldFill)"/>
      <rect x="0" y="0" width="630" height="28" fill="#c99a18"/>
      <path d="M0 450 Q370 385 630 440 V462 Q370 407 0 472 Z" fill="#a82a2a"/>
      <rect x="0" y="960" width="630" height="80" fill="#a82a2a"/>
      <rect x="0" y="960" width="630" height="6" fill="#7d1b1b"/>
    </svg>

    <div class="brand-box">
      <span class="brand-dot"></span>
      <span class="brand-name">TROVELLA</span>
    </div>

    <h1 class="product-title">
      <span class="title-line-1">MACADAMIA</span>
      <span class="title-line-2">NUTS</span>
    </h1>

    <ul class="benefits">
      <li>No cholestrol</li>
      <li>High in Omega 3, Monounsaturated Fats, Fibre</li>
      <li>Main source of antioxidant ptolemeic acid</li>
      <li>Highest level of monounsaturated fats of any commercial food</li>
      <li>Contains no GMO's</li>
    </ul>

    <div class="product-photo" role="img" aria-label="Photo of macadamia nuts in shell, some cracked open, on green leaves"></div>

    <p class="net-weight">300 g | 10.58 oz</p>
    <div class="free-tag">FREE CRACHER!</div>
    <div class="cracker-preview" role="img" aria-label="Image of the aluminium hand nut cracker"></div>
  </section>
</main>
</body>
</html>
```